[AMAZING DESIGN NEEDED] Women's Fishing Squeeze Page

I need a professional design for a landing page that is going to collect email addresses.

You can use the creatives already on the page or you can pull images from the facebook/instagram pages.
https://www.facebook.com/LakesLuresBoots
https://www.instagram.com/lakesluresandboots/

This is the page that needs designed: https://lakesluresandboots.example/email-opt-in/

See attached for examples.

Target Market(s)

Women who like to go fishing

Industry/Entity Type

Fishing

Number of Pages Required

1 page

Font styles to use
Sans Serif

Requirements
Must have
• excellent design. Call to actions.

```html
<!DOCTYPE html>
<html lang="en">
<head>
<meta charset="utf-8">
<title>Lakes, Lures &amp; Boots — Sign Up</title>
<link href="https://fonts.googleapis.com/css2?family=Hind:wght@400;500;600&family=Dancing+Script:wght@600&display=swap" rel="stylesheet">
<style>
  :root{
    --brown:#4f3f31;
    --teal:#0d7e7e;
    --beige:#cbb9a8;
    --field:#e4e4e4;
    --white:#ffffff;
    --text:#2f2a26;
  }
  *{box-sizing:border-box;margin:0;padding:0}
  html,body{width:1200px;height:904px;overflow:hidden}
  body{position:relative;font-family:"Hind",sans-serif;color:var(--text);background:var(--beige)}
  a{color:inherit;text-decoration:none}

  .hero-photo{position:absolute;inset:0 0 auto 0;height:780px;
    background:linear-gradient(180deg,#c9dcef 0%,#b7cde4 14%,#8a8f7a 26%,#4d6b43 38%,#35552f 48%,#6d8fa0 56%,#4f7488 70%,#3e5f6e 100%)}

  .wave{position:absolute;left:0;top:0;width:1200px;height:904px}

  .brand{position:absolute;left:88px;top:42px;display:flex;align-items:center;gap:8px;
    font-size:20px;font-weight:600;color:var(--teal)}
  .brand-dot{width:14px;height:14px;border-radius:50%;background:var(--teal)}

  .util{position:absolute;top:24px;left:548px;height:32px;display:flex;align-items:center;font-size:15px;font-weight:500;color:var(--brown)}
  .util .sep{margin:0 14px}
  .circle-btn{position:absolute;top:24px;width:32px;height:32px;border-radius:50%;background:var(--brown);display:flex;align-items:center;justify-content:center}
  .search{left:847px}
  .social-a{left:1039px}
  .social-b{left:1079px}
  .cart{position:absolute;left:895px;top:24px;width:128px;height:32px;border-radius:16px;background:var(--teal);color:var(--white);
    display:flex;align-items:center;justify-content:center;gap:8px;font-size:15px;font-weight:600;letter-spacing:.5px}

  .main-nav{position:absolute;left:352px;top:80px;width:848px;height:40px;background:var(--brown);
    clip-path:polygon(32px 0,100% 0,100% 100%,0 100%)}
  .main-nav a{position:absolute;top:0;line-height:42px;color:var(--white);font-size:15px;font-weight:500;letter-spacing:.3px}

  .signup-card{position:absolute;left:616px;top:292px;width:496px;height:448px;background:var(--white);border-radius:14px}
  .card-badge{position:absolute;left:784px;top:212px;width:160px;height:160px;border-radius:50%;background:var(--white);
    display:flex;align-items:flex-start;justify-content:center;padding-top:50px;font-size:15px;font-weight:600;color:var(--teal)}
  .signup-title{position:absolute;left:616px;top:352px;width:496px;text-align:center;font-family:"Dancing Script",cursive;font-size:58px;font-weight:600;color:var(--brown)}
  .signup-sub{position:absolute;left:616px;top:436px;width:496px;text-align:center;font-size:24px;color:var(--text)}
  .signup-sub em{color:var(--teal);font-style:italic}
  .field{position:absolute;left:648px;width:432px;height:40px;border-radius:20px;background:var(--field);border:none;
    padding:4px 20px 0;font-family:inherit;font-size:15px;color:var(--text)}
  .field::placeholder{color:#3b3632}
  .subscribe{position:absolute;left:648px;top:658px;width:432px;height:40px;border-radius:20px;border:none;background:var(--teal);
    color:var(--white);font-family:inherit;font-size:15px;font-weight:600;letter-spacing:.6px;padding-top:3px}

  .footer-brand{position:absolute;left:180px;top:660px;display:flex;align-items:center;gap:14px;font-size:34px;font-weight:600;color:var(--teal)}
  .footer-brand .brand-dot{width:28px;height:28px}
  .copyright{position:absolute;left:88px;top:835px;font-size:15px;color:var(--brown)}
  .payments{position:absolute;left:450px;top:833px;display:flex;gap:18px;font-size:14px;font-weight:600;color:var(--brown)}
  .foot-social{position:absolute;top:823px;width:40px;height:40px;border-radius:50%}
  .foot-a{left:1023px;background:var(--teal)}
  .foot-b{left:1071px;background:var(--brown)}
</style>
</head>
<body>
  <div class="hero-photo" role="img" aria-label="Woman fly fishing knee-deep in a mountain lake with pine-covered slopes and blue sky"></div>

  <svg class="wave" viewBox="0 0 1200 904" aria-hidden="true">
    <path fill="#4f3f31" d="M0,652 C110,596 210,566 296,566 C420,568 520,630 640,680 C740,722 820,760 900,762 C1000,764 1100,720 1200,640 L1200,904 L0,904Z"/>
    <path fill="#cbb9a8" d="M0,676 C110,620 210,592 296,592 C420,594 520,650 640,700 C740,742 820,784 900,784 C1000,782 1100,730 1200,690 L1200,904 L0,904Z"/>
  </svg>

  <header>
    <a class="brand" href="#"><span class="brand-dot"></span>LakesLuresBoots</a>
    <div class="util"><a href="#">Gift Certificates</a><span class="sep">|</span><a href="#">Sign in or Register</a></div>
    <a class="circle-btn search" href="#" aria-label="Search">
      <svg width="14" height="14" viewBox="0 0 14 14" fill="none" stroke="#fff" stroke-width="1.4"><circle cx="8" cy="6" r="4.5"/><path d="M4.8 9.2 1 13"/></svg>
    </a>
    <a class="cart" href="#">
      <svg width="14" height="12" viewBox="0 0 14 12" fill="none" stroke="#fff" stroke-width="1.3"><path d="M0 1h2.5l1.8 7h7.5L13 3H3.3"/><circle cx="5" cy="10.5" r="1"/><circle cx="11" cy="10.5" r="1"/></svg>
      Cart $0.00
    </a>
    <a class="circle-btn social-a" href="#" aria-label="Our social page"></a>
    <a class="circle-btn social-b" href="#" aria-label="Our photo page"></a>
    <nav class="main-nav">
      <a href="#" style="left:70px">CLOTHING</a>
      <a href="#" style="left:180px">HATS</a>
      <a href="#" style="left:251px">BUNDLES</a>
      <a href="#" style="left:351px">ACCESSORIES &amp; STICKERS</a>
      <a href="#" style="left:570px">JEWELRY</a>
      <a href="#" style="left:673px">CLEARANCE</a>
    </nav>
  </header>

  <div class="footer-brand"><span class="brand-dot"></span>LakesLuresBoots</div>

  <form class="signup" action="https://lakesluresandboots.example/email-opt-in/">
    <div class="card-badge">LakesLuresBoots</div>
    <div class="signup-card"></div>
    <h1 class="signup-title">Sign Up Today</h1>
    <p class="signup-sub">And receive <em>15% off</em> your next order</p>
    <input class="field" style="top:490px" type="text" placeholder="First Name">
    <input class="field" style="top:546px" type="text" placeholder="Last Name">
    <input class="field" style="top:602px" type="email" placeholder="Email Address *">
    <button class="subscribe" type="submit">SUBSCRIBE AND SAVE</button>
  </form>

  <footer>
    <p class="copyright">© 2021 Lakes, Lures &amp; Boots</p>
    <div class="payments"><span>NorthPay</span><span>Ferncard</span><span>Loonpay</span><span>Cedar</span><span>Tally</span></div>
    <a class="foot-social foot-a" href="#" aria-label="Our social page"></a>
    <a class="foot-social foot-b" href="#" aria-label="Our photo page"></a>
  </footer>
</body>
</html>
```